Rock band business card design

I need an edgy double sided business card to hand out at music events and to send out to radio.

It needs to display our logo, web address and social media icons (plazzo, chirpex, sonicvaultly).

Colour scheme to match our website (www.torvelkash.com)

Please include this quote:
Bright embers rising... a stirring... TORVEL KASH.

Logo files have been attached.

I look forward to seeing your designs!

Target Market(s)

radio stations, music fans.

Industry/Entity Type

Events

Requirements
Must have
• Website address, social media icons, quote, colour scheme to match www.torvelkash.com

```html
<!DOCTYPE html>
<html lang="en">
<head>
<meta charset="utf-8">
<title>Torvel Kash — Business Card</title>
<link rel="stylesheet" href="https://fonts.googleapis.com/css2?family=Oswald:wght@300;500;700&display=swap">
<style>
  :root {
    --backdrop: #d9d6d1;
    --card-white: #f2f1ee;
    --ink: #1b1714;
    --ink-soft: #3a332d;
    --sand-light: #f3d39a;
    --sand: #d08a3c;
    --sand-deep: #8c4a1a;
    --umber: #4a2410;
    --accent-red: #d8262b;
    --type-light: #fbf6ee;
  }
  * { margin: 0; padding: 0; box-sizing: border-box; }
  html, body { width: 1200px; height: 873px; overflow: hidden; }
  body {
    background: var(--backdrop);
    font-family: "Oswald", "Arial Narrow", sans-serif;
    display: flex;
    align-items: center;
    justify-content: center;
    gap: 40px;
  }
  .card {
    width: 540px;
    height: 309px;
    display: block;
    box-shadow: 0 6px 18px rgba(0,0,0,0.18);
  }
  .card text { font-family: "Oswald", "Arial Narrow", sans-serif; }
  .web-prefix, .web-suffix { font-weight: 300; font-size: 15px; fill: var(--ink-soft); letter-spacing: 1px; }
  .band-name { font-weight: 500; font-size: 46px; fill: var(--ink); letter-spacing: 4px; }
  .social-light { font-weight: 500; font-size: 15px; fill: var(--type-light); letter-spacing: 1px; text-transform: uppercase; }
  .social-dark { font-weight: 500; font-size: 17px; fill: var(--ink); letter-spacing: 1px; }
  .quote-line { font-weight: 500; font-size: 22px; fill: var(--type-light); letter-spacing: 1px; }
  .quote-name { font-weight: 700; font-size: 30px; fill: var(--type-light); letter-spacing: 1px; }
  .emblem-name { font-weight: 500; font-size: 22px; fill: var(--type-light); letter-spacing: 3px; }
</style>
</head>
<body>

  <!-- Front face -->
  <svg class="card card-front" viewBox="0 0 540 309" xmlns="http://www.w3.org/2000/svg">
    <defs>
      <linearGradient id="desert-front" x1="0" y1="0" x2="1" y2="1">
        <stop offset="0" stop-color="var(--sand-light)"/>
        <stop offset="0.45" stop-color="var(--sand)"/>
        <stop offset="1" stop-color="var(--sand-deep)"/>
      </linearGradient>
    </defs>
    <rect class="desert-scene" width="540" height="309" fill="url(#desert-front)" role="img" aria-label="Desert pyramids at sunrise, warm amber light"/>
    <polygon class="white-band" points="150,0 540,0 540,170 400,309 0,309 0,140" fill="var(--card-white)"/>
    <line class="band-rule" x1="20" y1="118" x2="128" y2="10" stroke="var(--type-light)" stroke-width="0.8" opacity="0.8"/>
    <line class="band-rule" x1="420" y1="298" x2="530" y2="188" stroke="var(--type-light)" stroke-width="0.8" opacity="0.8"/>

    <text class="web-prefix" x="170" y="118">www.</text>
    <text class="band-name" x="270" y="168" text-anchor="middle">TORVEL KASH</text>
    <text class="web-suffix" x="372" y="192">.com</text>

    <rect x="18" y="18" width="10" height="10" fill="var(--type-light)"/>
    <text class="social-light" x="34" y="28">plazzo</text>

    <circle cx="24" cy="283" r="6" fill="var(--accent-red)"/>
    <text class="social-dark" x="36" y="289">SONICVAULTLY</text>

    <circle cx="462" cy="285" r="5" fill="var(--type-light)"/>
    <text class="social-light" x="472" y="290">chirpex</text>
  </svg>

  <!-- Back face -->
  <svg class="card card-back" viewBox="0 0 540 309" xmlns="http://www.w3.org/2000/svg">
    <defs>
      <linearGradient id="desert-back" x1="1" y1="0" x2="0" y2="1">
        <stop offset="0" stop-color="var(--sand-light)"/>
        <stop offset="0.35" stop-color="var(--sand)"/>
        <stop offset="0.75" stop-color="var(--sand-deep)"/>
        <stop offset="1" stop-color="var(--umber)"/>
      </linearGradient>
    </defs>
    <rect class="desert-scene" width="540" height="309" fill="url(#desert-back)" role="img" aria-label="Pyramids in the desert under a rising sun and a large pale planet"/>

    <text class="quote-line" x="28" y="48">BRIGHT EMBERS RISING...</text>

    <text class="emblem-name" x="300" y="130" text-anchor="middle">TORVEL KASH</text>

    <text class="quote-line" x="512" y="236" text-anchor="end">A STIRRING...</text>
    <text class="quote-name" x="512" y="276" text-anchor="end">TORVEL KASH.</text>
  </svg>

</body>
</html>
```